Brantley Estates is a commercial real estate development company based in the United States. We develop high-end office buildings and student housing apartments. We have a new logo and need to update all of our stationary items and business cards. We would like the design to be clean and professional. Our logo and color information is attached. Our logo MUST be in full color and not as white. It is preferred that the logo is on a white background.

Color code Blue R 0. G 62. B 124 ( #003E7C )
C 100 M84 Y 26 K 22
Black R32. G30. B30 ( #201E1E)
C100 M100 Y100 K100

Font used TRAJAN PRO3 PRO BOLD.

Items needed:
1. Business card - Leaning towards doing just a one side business card in a thicker paper. Include - logo, name - Martin E. Caldwell, Title - Chairman & CEO, 5120 Ridgemont Pkwy. Suite 400, Atlanta, GA 30327 - Cell number 404.617.####, Office 770.245.62## email@brantleyestates.com; www.brantleyestates.com.

2. Letterhead - Standard 8.5 by 11 paper. We do have a smaller size for the CEO that is 7.25 by 10.5 that is just a mirror of the letterhead except with his name (Martin E. Caldwell) and title (Chariman & CEO) listed at the top in the header. Letthead needs address, phone number and website, plus logo. *Prepared such that we can either implement as a Google Document template or professionally print.

3. Legal sized envelope - #10 envelope - which measures 4 1/8" by 9 1/2". We also use the same size envelope with a window. Need logo and address. A photo of the old envelope style is attached.

4. 9" x 12" Pocket folder - Need a design that can also be split to be a cover page and back - We use the cover pages in spiral binding machine, so we need to leave room on the left for that. One of the pockets should hold a business card. Include logo, address, phone, website. Also if text is needed, we could say development / leasing / property management.

5. Shipping label - 3 1/3" x 4" inches and 6 per page. Just need logo and address listed at top of the label and white space at bottom.

Company: Brantley Estates
Address: 5120 Ridgemont Pkwy. Suite 400, Atlanta, GA 30327
Phone: 770.245.6274
Fax: 770.245.6219 (probably not needed)
Website: www.brantleyestates.com

Thank you for all your help!

Target Market(s)

Should communicate a strong corporate feel

Contact Information for Business Card

Include - logo, name - Martin E. Caldwell, Title - Chairman & CEO, 5120 Ridgemont Pkwy. Suite 400, Atlanta, GA 30327 - Cell number 404.617.####, Office 770.245.62## email@brantleyestates.com; www.brantleyestates.com.

Logo Text

Brantley Estates

Colors

Designer to choose colors to be used in the design.

Requirements
Must have
• Our logo MUST be in full color and not as white. It is preferred that the logo is on a white background.
• Colors - Color code Blue R 0. G 62. B 124 ( #003E7C )
• C 100 M84 Y 26 K 22
Nice to have
• Font used in logo TRAJAN PRO3 PRO BOLD. Would love to see options of both a one sided and double-sided.
Should not have
• Logo in white.

```html
<!DOCTYPE html>
<html lang="en">
<head>
<meta charset="utf-8">
<title>Brantley Estates — Stationery Suite</title>
<link rel="stylesheet" href="https://fonts.googleapis.com/css2?family=Open+Sans:wght@400;600;700&display=swap">
<style>
  :root {
    --brand-blue: #003e7c;
    --folder-blue: #26397c;
    --ink: #201e1e;
    --paper: #ffffff;
    --stage-grey: #c9c9c9;
    --stage-dark: #1b1b1b;
    --stage-wood: #b48a63;
    --label-line: #9a9a9a;
  }
  * { box-sizing: border-box; margin: 0; padding: 0; }
  html, body { width: 1200px; height: 3511px; overflow: hidden; }
  body { font-family: "Open Sans", Arial, sans-serif; color: var(--ink); background: var(--paper); position: relative; }

  .section { position: absolute; left: 0; width: 1200px; overflow: hidden; }
  .section--stationery { top: 0; height: 800px; background: var(--stage-grey); }
  .section--cards { top: 800px; height: 863px; background: var(--stage-dark); }
  .section--envelopes { top: 1663px; height: 797px; background: var(--stage-wood); }
  .section--labels { top: 2460px; height: 1051px; background: var(--paper); }

  .piece { position: absolute; }

  /* Brand name lockup — always full colour */
  .brand { display: flex; align-items: center; gap: 8px; color: var(--brand-blue); font-weight: 700; text-transform: uppercase; line-height: 1.05; white-space: nowrap; }
  .brand__dot { flex: none; border-radius: 50%; background: currentColor; }
  .brand--plate { background: var(--paper); border-radius: 4px; }

  /* Letterhead */
  .letterhead { left: 91px; top: 24px; width: 468px; height: 629px; background: var(--paper); padding: 22px 26px 0; }
  .letterhead .brand { font-size: 15px; }
  .letterhead .brand__dot { width: 26px; height: 26px; }
  .letterhead__header { display: flex; justify-content: space-between; align-items: flex-start; }
  .letterhead__signer { text-align: right; color: var(--brand-blue); font-size: 11px; font-weight: 700; line-height: 1.3; margin-top: 4px; }
  .letterhead__body { margin-top: 40px; font-size: 7.3px; line-height: 1.55; color: var(--ink); }
  .letterhead__body p { margin-bottom: 7px; }
  .letterhead__footer { position: absolute; left: 26px; right: 26px; bottom: 18px; border-top: 1px solid #bbb; padding-top: 7px; display: flex; justify-content: space-between; font-size: 5.6px; line-height: 1.45; color: var(--ink); }
  .letterhead__footer div { border-left: 1px solid #bbb; padding-left: 5px; }
  .letterhead__footer div:first-child { border-left: none; padding-left: 0; }
  .letterhead__footer strong { color: var(--brand-blue); }
  .letterhead__bar { position: absolute; left: 0; right: 0; bottom: 0; height: 8px; background: var(--folder-blue); }

  /* Folder */
  .folder { left: 600px; top: 60px; width: 509px; height: 725px; background: var(--folder-blue); display: flex; align-items: center; justify-content: center; }
  .folder .brand { font-size: 34px; gap: 14px; padding: 16px 22px; }
  .folder .brand__dot { width: 52px; height: 52px; }

  /* Small cards in stationery row */
  .mini-card { top: 665px; height: 117px; }
  .mini-card--front { left: 125px; width: 127px; background: var(--paper); padding: 10px 8px; font-size: 5.5px; line-height: 1.4; }
  .mini-card--front .brand { font-size: 8px; gap: 4px; margin-bottom: 8px; }
  .mini-card--front .brand__dot { width: 12px; height: 12px; }
  .mini-card--back { left: 341px; width: 216px; background: var(--folder-blue); display: flex; align-items: center; justify-content: center; }
  .mini-card--back .brand { font-size: 12px; gap: 6px; padding: 6px 9px; }
  .mini-card--back .brand__dot { width: 18px; height: 18px; }

  /* Business cards */
  .card { top: 290px; width: 470px; height: 280px; }
  .card--back { left: 90px; background: var(--folder-blue); display: flex; align-items: center; justify-content: center; }
  .card--back .brand { font-size: 26px; gap: 12px; padding: 12px 18px; }
  .card--back .brand__dot { width: 40px; height: 40px; }
  .card--front { left: 640px; background: var(--paper); padding: 30px 30px; display: flex; gap: 28px; }
  .card--front .brand { font-size: 18px; flex-direction: column; align-items: flex-start; gap: 10px; width: 130px; }
  .card--front .brand__dot { width: 34px; height: 34px; }
  .card__person { color: var(--brand-blue); font-size: 22px; font-weight: 600; line-height: 1.15; }
  .card__title { color: var(--ink); font-size: 14px; margin-bottom: 14px; }
  .card__details { font-size: 13px; line-height: 1.4; color: var(--ink); }
  .card__details .accent { color: var(--brand-blue); font-weight: 600; }
  .card__web { margin-top: 10px; font-size: 13px; }

  /* Envelopes */
  .envelope { left: 276px; width: 720px; background: var(--paper); }
  .envelope--back { top: 31px; height: 336px; }
  .envelope--back svg { position: absolute; inset: 0; }
  .envelope--back .brand { position: absolute; left: 50%; top: 30px; transform: translateX(-50%); font-size: 20px; gap: 10px; padding: 8px 14px; }
  .envelope--back .brand__dot { width: 30px; height: 30px; }
  .envelope--front { top: 480px; height: 269px; padding: 26px 30px; }
  .envelope--front .brand { font-size: 17px; gap: 8px; }
  .envelope--front .brand__dot { width: 28px; height: 28px; }
  .envelope__address { margin-top: 6px; font-size: 11px; line-height: 1.35; color: var(--ink); width: 220px; }
  .envelope__strip { position: absolute; left: 0; right: 0; bottom: 0; height: 14px; background: var(--folder-blue); }

  /* Shipping labels */
  .label { width: 562px; height: 456px; border: 2px solid var(--label-line); border-radius: 22px; background: var(--paper); padding: 40px 0 0 62px; }
  .label .brand { font-size: 40px; gap: 14px; }
  .label .brand__dot { width: 58px; height: 58px; }
  .label__address { margin: 6px 0 0 72px; font-size: 13px; color: var(--ink); }
  .label--r1c1 { left: 24px; top: 72px; }
  .label--r1c2 { left: 614px; top: 72px; }
  .label--r2c1 { left: 24px; top: 547px; }
  .label--r2c2 { left: 614px; top: 547px; }
  .label--r3c1 { left: 24px; top: 1020px; }
  .label--r3c2 { left: 614px; top: 1020px; }
</style>
</head>
<body>

<section class="section section--stationery">
  <article class="piece letterhead">
    <header class="letterhead__header">
      <div class="brand"><span class="brand__dot"></span><span>Brantley<br>Estates</span></div>
      <div class="letterhead__signer">Martin E. Caldwell<br>Chairman &amp; CEO</div>
    </header>
    <div class="letterhead__body">
      <p>Thank you for your continued interest in our office and residential projects across the Atlanta region. Our team remains committed to thoughtful planning, careful construction and attentive management at every stage of a development. We believe each building should serve its tenants well for decades, and we work closely with architects, lenders and local partners to make that happen. Please find enclosed the current leasing summary along with the schedule for upcoming site tours.</p>
      <p>Our student housing communities continue to see strong demand near campus, and the newest phase is scheduled to open ahead of the fall semester. We are also finishing interior work on two office buildings, with several suites still available for lease. If you would like to review floor plans or discuss terms, our leasing staff will gladly arrange a meeting at a time that suits you.</p>
      <p>We appreciate your trust and look forward to working with you on the next project.</p>
    </div>
    <footer class="letterhead__footer">
      <div><strong>BRANTLEY ESTATES</strong><br>5120 Ridgemont Pkwy. Suite 400<br>Atlanta, GA 30327</div>
      <div>Cell number 404.617.####<br>Office 770.245.62##</div>
      <div>email@brantleyestates.com<br>www.brantleyestates.com</div>
    </footer>
    <div class="letterhead__bar"></div>
  </article>

  <div class="piece folder">
    <div class="brand brand--plate"><span class="brand__dot"></span><span>Brantley<br>Estates</span></div>
  </div>

  <div class="piece mini-card mini-card--front">
    <div class="brand"><span class="brand__dot"></span><span>Brantley<br>Estates</span></div>
    <div>Martin E. Caldwell<br>Chairman &amp; CEO</div>
    <div>Off 770.245.62##<br>Cell 404.617.####</div>
    <div>www.brantleyestates.com</div>
  </div>
  <div class="piece mini-card mini-card--back">
    <div class="brand brand--plate"><span class="brand__dot"></span><span>Brantley<br>Estates</span></div>
  </div>
</section>

<section class="section section--cards">
  <div class="piece card card--back">
    <div class="brand brand--plate"><span class="brand__dot"></span><span>Brantley<br>Estates</span></div>
  </div>
  <div class="piece card card--front">
    <div class="brand"><span class="brand__dot"></span><span>Brantley<br>Estates</span></div>
    <div class="card__info">
      <div class="card__person">Martin E. Caldwell</div>
      <div class="card__title">Chairman &amp; CEO</div>
      <div class="card__details">
        <span class="accent">BRANTLEY ESTATES</span><br>
        5120 Ridgemont Pkwy.<br>Suite 400, Atlanta, GA 30327<br>
        <span class="accent">Off</span> 770.245.62##<br>
        <span class="accent">Cell</span> 404.617.####<br>
        email@brantleyestates.com
      </div>
      <div class="card__web">www.brantleyestates.com</div>
    </div>
  </div>
</section>

<section class="section section--envelopes">
  <div class="piece envelope envelope--back">
    <svg width="720" height="336" viewBox="0 0 720 336" aria-hidden="true">
      <path d="M0 336 L300 150 Q360 120 420 150 L720 336 Z" fill="#f1f1f1"/>
      <path d="M0 0 L0 336 L300 150 Z" fill="#f7f7f7"/>
      <path d="M720 0 L720 336 L420 150 Z" fill="#f7f7f7"/>
      <path d="M0 0 H720 V40 Q720 70 660 85 L400 140 Q360 150 320 140 L60 85 Q0 70 0 40 Z" fill="var(--folder-blue)"/>
    </svg>
    <div class="brand brand--plate"><span class="brand__dot"></span><span>Brantley<br>Estates</span></div>
  </div>
  <div class="piece envelope envelope--front">
    <div class="brand"><span class="brand__dot"></span><span>Brantley<br>Estates</span></div>
    <p class="envelope__address">5120 Ridgemont Pkwy. Suite 400<br>Atlanta, GA 30327</p>
    <div class="envelope__strip"></div>
  </div>
</section>

<section class="section section--labels">
  <div class="piece label label--r1c1"><div class="brand"><span class="brand__dot"></span><span>Brantley<br>Estates</span></div><p class="label__address">5120 Ridgemont Pkwy. Suite 400, Atlanta, GA 30327</p></div>
  <div class="piece label label--r1c2"><div class="brand"><span class="brand__dot"></span><span>Brantley<br>Estates</span></div><p class="label__address">5120 Ridgemont Pkwy. Suite 400, Atlanta, GA 30327</p></div>
  <div class="piece label label--r2c1"><div class="brand"><span class="brand__dot"></span><span>Brantley<br>Estates</span></div><p class="label__address">5120 Ridgemont Pkwy. Suite 400, Atlanta, GA 30327</p></div>
  <div class="piece label label--r2c2"><div class="brand"><span class="brand__dot"></span><span>Brantley<br>Estates</span></div><p class="label__address">5120 Ridgemont Pkwy. Suite 400, Atlanta, GA 30327</p></div>
  <div class="piece label label--r3c1"></div>
  <div class="piece label label--r3c2"></div>
</section>

</body>
</html>
```